Business Card Design Project

Need business card for new non profit organization that includes the attached logo in some form.
with this information
Name: Marcus Holloway Treff
Title: President & Founder
A: P.O. Box 61537, Portland, Oregon, 97451-6153
E: marc@hollowaytrust.org
E: marc@marctreff.com
P: 1.971.555.0172

Industry/Entity Type
Non Profit

```html
<!DOCTYPE html>
<html lang="en">
<head>
<meta charset="utf-8">
<title>Holloway Trust — Business Card</title>
<link href="https://fonts.googleapis.com/css2?family=Cinzel:wght@400;500&family=Jost:wght@400;500&display=swap" rel="stylesheet">
<style>
  :root {
    --bg: #2a2a2c;
    --card: #ffffff;
    --ink: #2b2a6e;
    --divider: #e4e4ea;
  }
  * { box-sizing: border-box; margin: 0; padding: 0; }
  html, body { width: 1200px; height: 900px; overflow: hidden; }
  body { background: var(--bg); position: relative; }
  .card {
    position: absolute; left: 75px; top: 150px;
    width: 1050px; height: 600px;
    background: var(--card);
    color: var(--ink);
    box-shadow: 0 18px 40px rgba(0,0,0,.45);
  }
  .card__divider {
    position: absolute; left: 440px; top: 0; bottom: 0;
    width: 1px; background: var(--divider);
  }
  .brand {
    position: absolute; left: 0; top: 0; width: 440px; height: 600px;
    display: flex; align-items: center; justify-content: center; gap: 14px;
  }
  .brand__mark {
    width: 26px; height: 26px; border-radius: 50%; background: var(--ink);
  }
  .brand__name {
    font-family: "Jost", sans-serif; font-weight: 500;
    font-size: 34px; letter-spacing: 1px; color: var(--ink);
  }
  .identity {
    position: absolute; right: 60px; top: 62px; text-align: right;
  }
  .identity__name {
    font-family: "Cinzel", serif; font-weight: 400;
    font-size: 36px; letter-spacing: 1px;
  }
  .identity__title {
    font-family: "Jost", sans-serif; font-size: 20px; margin-top: 4px;
  }
  .contact {
    position: absolute; left: 540px; top: 240px;
    list-style: none;
    font-family: "Jost", sans-serif; font-size: 23px; line-height: 30px;
  }
  .contact__item { display: flex; align-items: flex-start; gap: 18px; margin-bottom: 4px; }
  .contact__icon { width: 20px; height: 20px; margin-top: 5px; flex: none; fill: var(--ink); }
</style>
</head>
<body>
  <section class="card">
    <div class="brand">
      <span class="brand__mark"></span>
      <span class="brand__name">Holloway Trust</span>
    </div>
    <div class="card__divider"></div>

    <header class="identity">
      <h1 class="identity__name">Marcus Holloway Treff</h1>
      <p class="identity__title">President &amp; Founder</p>
    </header>

    <ul class="contact">
      <li class="contact__item">
        <svg class="contact__icon" viewBox="0 0 20 20"><path d="M10 1a6 6 0 0 0-6 6c0 4.5 6 12 6 12s6-7.5 6-12a6 6 0 0 0-6-6zm0 8.2A2.2 2.2 0 1 1 10 4.8a2.2 2.2 0 0 1 0 4.4z"/></svg>
        <span>P.O. Box 61537<br>Portland, OR<br>97451-6153</span>
      </li>
      <li class="contact__item">
        <svg class="contact__icon" viewBox="0 0 20 20"><path d="M2 5h16v10H2z M2 5l8 6 8-6" fill="none" stroke="#2b2a6e" stroke-width="1.8"/></svg>
        <span>marc@hollowaytrust.org</span>
      </li>
      <li class="contact__item">
        <svg class="contact__icon" viewBox="0 0 20 20"><path d="M2 5h16v10H2z M2 5l8 6 8-6" fill="none" stroke="#2b2a6e" stroke-width="1.8"/></svg>
        <span>marc@marctreff.com</span>
      </li>
      <li class="contact__item">
        <svg class="contact__icon" viewBox="0 0 20 20"><path d="M5 2l3 4-2 2c1 2.5 3.5 5 6 6l2-2 4 3-2 3C9 18 2 11 2 4z"/></svg>
        <span>1.971.555.0172</span>
      </li>
      <li class="contact__item">
        <svg class="contact__icon" viewBox="0 0 20 20"><path d="M5 2l3 4-2 2c1 2.5 3.5 5 6 6l2-2 4 3-2 3C9 18 2 11 2 4z"/></svg>
        <span>1.541.555.0148</span>
      </li>
    </ul>
  </section>
</body>
</html>
```